Varneck Law Business cards and stationary design project

We are looking for a stationary design for business cards (double sided), 8x10, 5x7, and legal and standard envelopes.

We would like the design to match the logo that we have already.
Color palate preferred is Teal, White, grey and any others that will look good for a professional law firm.

We would like this statement: "RELATIONSHIPS. RESPECT. RESULT" to be on the back of the business cards and maybe on the stationary if it looks good.

Please see link to website for more information: www.varneck-law-example.com

Target Market(s)

Potential clients that need Attorney services.

Industry/Entity Type

Law Firm

Contact Information for Business Card

We would like the front and back to be two different colors. Current business cards are teal front, grey back and are a vertical design. We are open to options with colors.

Font styles to use
Serif

Colors
33a6d7
33b8a4
b9b9b9
5c5c5c

Requirements
Must have
• Logo supplied needs to go on the card and stationary.
• Match website color palate, www.varneck-law-example.com
• Be professional and not too wordy.
• Criminal Law, Civil Litigation, Personal Injury, Restraining Orders need to be on the card.
Nice to have
• RELATIONSHIPS. RESPECT. RESULTS. on the back of the card.
Should not have
• Not be too busy/wordy or too flashy.

```html
<!DOCTYPE html>
<html lang="en">
<head>
<meta charset="utf-8">
<title>Varneck Law – Business Card</title>
<link rel="stylesheet" href="https://fonts.googleapis.com/css2?family=Cinzel:wght@400;600&family=Crimson+Text:wght@400&display=swap">
<style>
  :root {
    --teal: #10889a;
    --white: #ffffff;
    --ink: #555a5e;
    --backdrop: #e4e6e7;
  }
  * { box-sizing: border-box; margin: 0; padding: 0; }
  html, body { width: 1105px; height: 1200px; overflow: hidden; }
  body {
    background: var(--backdrop);
    position: relative;
    font-family: "Crimson Text", Georgia, serif;
  }
  .card {
    position: absolute;
    left: 192px;
    width: 720px;
    height: 412px;
  }
  .card--front { top: 150px; background: var(--white); }
  .card--back { top: 606px; background: var(--teal); }

  .firm-mark {
    position: absolute;
    left: 225px;
    top: 166px;
    transform: translateX(-50%);
    display: flex;
    align-items: center;
    gap: 12px;
    white-space: nowrap;
  }
  .firm-mark__dot {
    width: 12px; height: 12px; border-radius: 50%;
    background: var(--teal);
  }
  .firm-mark__name {
    font-family: "Cinzel", "Times New Roman", serif;
    font-size: 32px;
    color: var(--teal);
    letter-spacing: 1px;
  }

  .person {
    position: absolute;
    left: 376px;
    top: 108px;
  }
  .person__name {
    font-family: "Cinzel", "Times New Roman", serif;
    font-weight: 600;
    font-size: 31px;
    line-height: 1;
    color: var(--teal);
    letter-spacing: 0.5px;
  }
  .person__title {
    font-family: "Cinzel", "Times New Roman", serif;
    font-size: 21px;
    color: var(--ink);
    margin-top: 6px;
    letter-spacing: 0.5px;
  }
  .contact {
    list-style: none;
    margin-top: 20px;
  }
  .contact__item {
    display: flex;
    align-items: center;
    gap: 14px;
    font-size: 21px;
    line-height: 31px;
    color: var(--ink);
  }
  .contact__icon { width: 16px; height: 16px; fill: var(--teal); flex: none; }

  .practice-band {
    position: absolute;
    left: 0; bottom: 0;
    width: 100%; height: 38px;
    background: var(--teal);
    color: var(--white);
    font-size: 21px;
    line-height: 38px;
    text-align: center;
    letter-spacing: 0.2px;
  }

  .back-name {
    position: absolute;
    left: 0; right: 0; top: 150px;
    text-align: center;
    font-family: "Cinzel", "Times New Roman", serif;
    font-size: 58px;
    color: var(--white);
    letter-spacing: 2px;
  }
  .tagline {
    position: absolute;
    left: 0; right: 0; top: 354px;
    text-align: center;
    font-family: "Cinzel", "Times New Roman", serif;
    font-size: 21px;
    color: var(--white);
    letter-spacing: 1px;
  }
</style>
</head>
<body>
  <section class="card card--front">
    <div class="firm-mark">
      <span class="firm-mark__dot"></span>
      <span class="firm-mark__name">Varneck Law</span>
    </div>

    <div class="person">
      <h1 class="person__name">Dana Merrow</h1>
      <p class="person__title">Trial Lawyer</p>
      <ul class="contact">
        <li class="contact__item">
          <svg class="contact__icon" viewBox="0 0 16 16" aria-hidden="true"><path d="M3.2 1 5.6 3.6 4.4 5.6c.9 2.2 2.9 4.3 6 6l2-1.2L15 12.8l-1.6 2.2C7 15 1 9 1 2.6z"/></svg>
          (555) 014-2290
        </li>
        <li class="contact__item">
          <svg class="contact__icon" viewBox="0 0 16 16" aria-hidden="true"><path d="M1 3h14v1.2L8 9 1 4.2z M1 5.6 8 10.4l7-4.8V13H1z"/></svg>
          dana@varneck-law-example.com
        </li>
        <li class="contact__item">
          <svg class="contact__icon" viewBox="0 0 16 16" aria-hidden="true"><circle cx="8" cy="8" r="7"/><path d="M3 6h3l1 2-2 3M10 3l1 3 3 1M9 13l1-3 3 0" stroke="#fff" stroke-width="1.2" fill="none"/></svg>
          www.varneck-law-example.com
        </li>
      </ul>
    </div>

    <div class="practice-band">Criminal Law | Civil Litigation/Personal Injury | Restraining</div>
  </section>

  <section class="card card--back">
    <p class="back-name">Varneck Law</p>
    <p class="tagline">RELATIONSHIPS. RESPECT. RESULTS.</p>
  </section>
</body>
</html>
```